Webbanner-Design für Handel von Edelmetallen
Zielgruppe
Handel (Kauf und Verkauf) von Edelmetallen -> Gold und Silber | Münzen und Barren
Zielgruppe ist der vermögende Privatkunde, so wie Sammler und Erstinvestoren die sich für eine Geldanlage in Gold- und Silber interessieren.
Aufgabenstellung
Wir benötigen Bannersets für 4 gängige Google Ads Größen für insgesamt 11 Kampagnen in DE und EN. Vorlage, Logo, lizenzierte Bilder werden geliefert.
Banner 468 Pixel 60 Pixel
Square 250 Pixel 250 Pixel
Large Rectangle 336 Pixel 280 Pixel
Skyscraper 120 Pixel 600 Pixel
Die 11 DE Kampagnen:
1) Branding:
Text:
Brantor Metall AG
Gold- | Silber- Münzen und -Barren
An- und Verkauf | Wertlagerung
2) Gold kaufen:
Goldmünzen und Goldbarren kaufen
Bestpreise | Versicherte Versendung
3) Silber kaufen
MwSt-freie Silbermünzen kaufen
4) Kurse gefallen
Gold und Silberpreise sind gefallen
Jetzt günstiger einkaufen und Durchschnittskosten verbilligen
5) Wertlagerung
Allokierte Wertlagerung bei Valkenra
ab 0,3% p.a. - täglich kündbar
Die ersten 3 Monate kostenfrei
Hier mehr erfahren
6) Wertagerung 2
Hochsicherheitswertlagerung zugänglich
für alle Bestellungen ab 100 Euro.
3 Monate kostenfrei.
7) Gold und Silber Krypto kaufen
Gold und Silber mit über 50 Krypto
Währungen kaufen
8) Semi-Numismatic
Die 5 besten Tipps für Münzen Sammler
9) Verkaufen
Gold und Silber an Brantor Metall verkaufen
Tageshöchstpreise | Versicherte Abholung
10) Sicheres Investment
Jetzt in das sicherste Investment aller Zeiten investieren: Gold
11) Silber Investment
Investment Chance der 20er: Silber
Hier kostenfrei informieren
Die 11 EN Kampagnen:
Gold- | Silver- Coins und -Bullion
Buy and Sell | Secure Storage
Buy Gold Coins and Gold Coins at
Best Price | Insured Global Delivery
Buy VAT Free Silvercoins
Buy the Dip!
Take a..

```html
<!DOCTYPE html>
<html lang="de">
<head>
<meta charset="utf-8">
<title>Brantor Metall – Bannerset</title>
<link href="https://fonts.googleapis.com/css2?family=Ubuntu:wght@400;500;700&display=swap" rel="stylesheet">
<style>
  :root{
    --page:#ffffff;
    --frame:#d9d9d9;
    --label:#c4c4c4;
    --ink:#1b1a16;
    --green:#2f7d2c;
    --tick:#236b22;
    --gold-light:#f7e6ad;
    --gold-mid:#e4bd68;
    --gold-deep:#b9873a;
    --bronze:#7a5a2c;
    --dusk:#2e2416;
    --btn-top:#f8e28e;
    --btn-bottom:#e2bb55;
    --badge:#e8e8e8;
    --badge-line:#c9c9c9;
    --badge-red:#d9463b;
  }
  html,body{margin:0;padding:0;width:772px;height:1200px;overflow:hidden;background:var(--page);}
  .sheet{
    position:relative;width:1208px;height:1877px;
    transform:scale(0.63907);transform-origin:0 0;
    box-sizing:border-box;border:1px solid var(--frame);
    font-family:"Ubuntu",sans-serif;color:var(--ink);
  }
  .size-label{position:absolute;margin:0;font-size:36px;font-weight:700;color:var(--label);}
  .ad-number{position:absolute;font-size:38px;font-weight:700;color:var(--label);line-height:1;}

  .ad{position:absolute;box-shadow:0 2px 8px rgba(0,0,0,.12);background:#fff;overflow:hidden;}
  .ad--rect{width:336px;height:280px;}
  .ad--sky{width:120px;height:600px;}
  .ad__stage{position:absolute;left:0;top:0;right:0;overflow:hidden;
    background:
      radial-gradient(ellipse 60% 70% at 35% 20%, rgba(255,250,225,.85), transparent 70%),
      linear-gradient(160deg,var(--gold-light) 0%,var(--gold-mid) 55%,var(--gold-deep) 82%,var(--bronze) 100%);}
  .ad--rect .ad__stage{height:220px;}
  .ad--sky .ad__stage{height:520px;
    background:
      radial-gradient(ellipse 90% 40% at 40% 15%, rgba(255,248,215,.85), transparent 70%),
      linear-gradient(180deg,var(--gold-mid) 0%,var(--gold-light) 30%,var(--gold-mid) 62%,var(--bronze) 88%,var(--dusk) 100%);}

  .ad__visual{position:absolute;border-radius:50%;
    background:radial-gradient(circle at 40% 40%, #fff6d2 0%, #e8c46c 40%, #b8893a 70%, rgba(160,120,50,0) 100%);}
  .ad__visual--silver{background:radial-gradient(circle at 40% 40%, #ffffff 0%, #d9d9d9 40%, #a9a9a9 68%, rgba(170,170,170,0) 100%);}

  .ad__copy{position:absolute;margin:0;padding:0;list-style:none;}
  .ad__headline{position:absolute;margin:0;font-weight:500;font-size:22px;line-height:25px;letter-spacing:.2px;}
  .ad--sky .ad__headline{font-size:19px;line-height:23px;}

  .bullets li{position:relative;font-size:20px;font-weight:500;line-height:22px;padding-left:14px;}
  .bullets li::before{content:"";position:absolute;left:0;top:9px;width:5px;height:5px;background:var(--green);}
  .ad--sky .bullets li{font-size:18px;line-height:20px;padding-left:10px;margin-bottom:9px;}
  .ad--sky .bullets li::before{top:8px;width:4px;height:4px;}

  .ticks li{position:relative;font-size:16px;line-height:20px;padding-left:20px;}
  .ticks .tick{position:absolute;left:0;top:1px;width:17px;height:17px;}
  .tick path{fill:none;stroke:var(--tick);stroke-width:2.6;stroke-linecap:round;stroke-linejoin:round;}
  .ad--sky .ticks li{font-size:15px;line-height:18px;margin-bottom:14px;}

  .cta{position:absolute;display:flex;align-items:center;justify-content:center;text-align:center;
    background:linear-gradient(180deg,var(--btn-top),var(--btn-bottom));border-radius:3px;
    color:var(--green);font-weight:500;font-size:15px;letter-spacing:.3px;text-decoration:none;
    box-shadow:0 1px 3px rgba(0,0,0,.25);}
  .ad--rect .cta{left:22px;height:34px;width:136px;}
  .ad--sky .cta{left:12px;top:457px;width:96px;height:46px;line-height:16px;}

  .ad__foot{position:absolute;left:0;right:0;bottom:0;background:#fff;}
  .ad--rect .ad__foot{height:60px;}
  .ad--sky .ad__foot{height:80px;}
  .pay{position:absolute;left:21px;top:22px;display:flex;gap:5px;}
  .pay span{display:block;width:37px;height:18px;border:1px solid var(--badge-line);background:var(--badge);box-sizing:border-box;}
  .pay span.pay--red{background:var(--badge-red);border-color:var(--badge-red);}
  .brand{position:absolute;display:flex;align-items:center;gap:5px;font-weight:500;color:var(--green);white-space:nowrap;}
  .brand i{display:block;border-radius:50%;border:2px solid var(--green);box-sizing:border-box;}
  .ad--rect .brand{right:12px;top:19px;font-size:17px;}
  .ad--rect .brand i{width:18px;height:18px;}
  .ad--sky .brand{left:0;right:0;justify-content:center;top:31px;font-size:13px;gap:4px;}
  .ad--sky .brand i{width:13px;height:13px;}
</style>
</head>
<body>
<svg width="0" height="0" style="position:absolute" aria-hidden="true">
  <symbol id="tick" viewBox="0 0 17 17"><path d="M2 10 L6 15 L15 2"/></symbol>
</svg>

<main class="sheet">
  <h2 class="size-label" style="left:145px;top:114px;">336 x 280</h2>

  <!-- Large Rectangle 1 -->
  <article class="ad ad--rect" style="left:143px;top:202px;">
    <div class="ad__stage">
      <div class="ad__visual ad__visual--silver" role="img" aria-label="Silbermünze mit Springbock-Motiv" style="left:238px;top:30px;width:120px;height:120px;"></div>
      <div class="ad__visual" role="img" aria-label="Goldmünze und 5-g-Feingoldbarren" style="left:170px;top:95px;width:190px;height:150px;"></div>
      <ul class="ad__copy bullets" style="left:17px;top:25px;">
        <li>Gold und Silber<br>Münzen und Barren</li>
        <li style="margin-top:8px;">An- und Verkauf</li>
        <li style="margin-top:10px;">Wertlagerung</li>
      </ul>
      <a class="cta" style="top:158px;">MEHR INFOS</a>
    </div>
    <footer class="ad__foot">
      <div class="pay"><span></span><span></span><span class="pay--red"></span></div>
      <div class="brand"><i></i>Brantor Metall</div>
    </footer>
  </article>
  <span class="ad-number" style="left:494px;top:200px;">1</span>

  <!-- Large Rectangle 2 -->
  <article class="ad ad--rect" style="left:728px;top:204px;">
    <div class="ad__stage">
      <div class="ad__visual" role="img" aria-label="Goldmünze mit Harfe und 5-g-Feingoldbarren" style="left:175px;top:40px;width:200px;height:200px;"></div>
      <h3 class="ad__headline" style="left:21px;top:19px;">Goldmünzen und<br>Goldbarren kaufen</h3>
      <ul class="ad__copy ticks" style="left:28px;top:79px;">
        <li><svg class="tick"><use href="#tick"/></svg>Bestpreise</li>
        <li style="margin-top:6px;"><svg class="tick"><use href="#tick"/></svg>Versicherte<br>Versendung</li>
      </ul>
      <a class="cta" style="top:162px;">MEHR INFOS</a>
    </div>
    <footer class="ad__foot">
      <div class="pay"><span></span><span></span><span class="pay--red"></span></div>
      <div class="brand"><i></i>Brantor Metall</div>
    </footer>
  </article>
  <span class="ad-number" style="left:696px;top:201px;">2</span>

  <!-- Large Rectangle 4 -->
  <article class="ad ad--rect" style="left:143px;top:591px;">
    <div class="ad__stage">
      <div class="ad__visual" role="img" aria-label="Goldmünze vor fallendem Kursverlauf" style="left:250px;top:40px;width:100px;height:100px;"></div>
      <div class="ad__visual ad__visual--silver" role="img" aria-label="Silbermünze mit Springbock-Motiv" style="left:195px;top:130px;width:110px;height:110px;"></div>
      <h3 class="ad__headline" style="left:21px;top:15px;">Gold und Silberpreise<br>sind gefallen</h3>
      <ul class="ad__copy ticks" style="left:22px;top:73px;">
        <li><svg class="tick"><use href="#tick"/></svg>Jetzt günstiger einkaufen</li>
        <li style="margin-top:6px;"><svg class="tick"><use href="#tick"/></svg>Durchschnittskosten<br>verbilligen</li>
      </ul>
      <a class="cta" style="top:162px;">MEHR INFOS</a>
    </div>
    <footer class="ad__foot">
      <div class="pay"><span></span><span></span><span class="pay--red"></span></div>
      <div class="brand"><i></i>Brantor Metall</div>
    </footer>
  </article>
  <span class="ad-number" style="left:490px;top:588px;">4</span>

  <!-- Large Rectangle 5 -->
  <article class="ad ad--rect" style="left:728px;top:591px;">
    <div class="ad__stage">
      <div class="ad__visual ad__visual--silver" role="img" aria-label="Silbermünze mit Ahornblatt vor Vorhängeschloss" style="left:230px;top:80px;width:120px;height:120px;"></div>
      <div class="ad__visual" role="img" aria-label="5-g-Feingoldbarren" style="left:180px;top:140px;width:140px;height:90px;"></div>
      <h3 class="ad__headline" style="left:21px;top:15px;">Allokierte Wertlagerung<br>bei Valkenra</h3>
      <ul class="ad__copy ticks" style="left:21px;top:73px;">
        <li><svg class="tick"><use href="#tick"/></svg>ab 0,3 % p.a.</li>
        <li style="margin-top:6px;"><svg class="tick"><use href="#tick"/></svg>täglich kündbar</li>
        <li style="margin-top:6px;"><svg class="tick"><use href="#tick"/></svg>die ersten 3 Monate<br>kostenlos</li>
      </ul>
      <a class="cta" style="top:173px;width:150px;">MEHR ERFAHREN</a>
    </div>
    <footer class="ad__foot">
      <div class="pay"><span></span><span></span><span class="pay--red"></span></div>
      <div class="brand"><i></i>Brantor Metall</div>
    </footer>
  </article>
  <span class="ad-number" style="left:696px;top:588px;">5</span>

  <h2 class="size-label" style="left:142px;top:971px;">120 x 600</h2>

  <!-- Skyscraper 1 -->
  <article class="ad ad--sky" style="left:143px;top:1070px;">
    <div class="ad__stage">
      <div class="ad__visual" role="img" aria-label="Goldmünze, Silbermünze und 5-g-Feingoldbarren" style="left:0;top:240px;width:140px;height:220px;"></div>
      <ul class="ad__copy bullets" style="left:11px;top:23px;">
        <li>Gold und<br>Silber<br>Münzen<br>und<br>Barren</li>
        <li>An- und<br>Verkauf</li>
        <li>Wert-<br>lagerung</li>
      </ul>
      <a class="cta">MEHR<br>ERFAHREN</a>
    </div>
    <footer class="ad__foot"><div class="brand"><i></i>Brantor Metall</div></footer>
  </article>
  <span class="ad-number" style="left:275px;top:1066px;">1</span>

  <!-- Skyscraper 2 -->
  <article class="ad ad--sky" style="left:410px;top:1070px;">
    <div class="ad__stage">
      <div class="ad__visual" role="img" aria-label="Goldmünze mit Harfe und 5-g-Feingoldbarren" style="left:10px;top:250px;width:140px;height:210px;"></div>
      <h3 class="ad__headline" style="left:15px;top:16px;">Gold-<br>münzen<br>und<br>Gold-<br>barren<br>kaufen</h3>
      <ul class="ad__copy ticks" style="left:10px;top:167px;">
        <li><svg class="tick"><use href="#tick"/></svg>Bestpreise</li>
        <li><svg class="tick"><use href="#tick"/></svg>Versicherte<br>Versendung</li>
      </ul>
      <a class="cta">MEHR<br>ERFAHREN</a>
    </div>
    <footer class="ad__foot"><div class="brand"><i></i>Brantor Metall</div></footer>
  </article>
  <span class="ad-number" style="left:542px;top:1066px;">2</span>

  <!-- Skyscraper 4 -->
  <article class="ad ad--sky" style="left:677px;top:1070px;">
    <div class="ad__stage">
      <div class="ad__visual" role="img" aria-label="Gold- und Silbermünze vor fallendem Kursverlauf" style="left:0;top:300px;width:130px;height:170px;"></div>
      <h3 class="ad__headline" style="left:15px;top:16px;">Gold und<br>Silber-<br>preise<br>sind<br>gefallen</h3>
      <ul class="ad__copy ticks" style="left:10px;top:146px;">
        <li><svg class="tick"><use href="#tick"/></svg>Jetzt<br>günstiger<br>einkaufen</li>
        <li><svg class="tick"><use href="#tick"/></svg>Durch-<br>schnitts-<br>kosten<br>verbilligen</li>
      </ul>
      <a class="cta">MEHR<br>ERFAHREN</a>
    </div>
    <footer class="ad__foot"><div class="brand"><i></i>Brantor Metall</div></footer>
  </article>
  <span class="ad-number" style="left:809px;top:1066px;">4</span>

  <!-- Skyscraper 5 -->
  <article class="ad ad--sky" style="left:944px;top:1070px;">
    <div class="ad__stage">
      <div class="ad__visual ad__visual--silver" role="img" aria-label="Silbermünze mit Ahornblatt vor Vorhängeschloss" style="left:20px;top:300px;width:120px;height:120px;"></div>
      <div class="ad__visual" role="img" aria-label="5-g-Feingoldbarren" style="left:0;top:380px;width:110px;height:80px;"></div>
      <h3 class="ad__headline" style="left:15px;top:22px;">Allokierte<br>Wert-<br>lagerung<br>bei<br>Valkenra</h3>
      <ul class="ad__copy ticks" style="left:10px;top:150px;">
        <li><svg class="tick"><use href="#tick"/></svg>ab 0,3 % p.a.</li>
        <li><svg class="tick"><use href="#tick"/></svg>täglich<br>kündbar</li>
        <li><svg class="tick"><use href="#tick"/></svg>die ersten<br>3 Monate<br>kostenlos</li>
      </ul>
      <a class="cta">MEHR<br>ERFAHREN</a>
    </div>
    <footer class="ad__foot"><div class="brand"><i></i>Brantor Metall</div></footer>
  </article>
  <span class="ad-number" style="left:1076px;top:1066px;">5</span>
</main>
</body>
</html>
```